ZELK LED WALL BUYERS GUIDE

We require a brcohure to send to our customers that sets out the provided text in a neat and clearly readable format, We wish to position this brochure as an information source that demonstrates us a market leader in this technology and not afraid to share what customers should be looking for in a new LED video wall. This will be used mostly in PDF format, will be multiple A4 pages and we are happy to include stock photos where required to further illustrate or show the technical nature of our business and products. Plenty of white space and easy to read is a MUST for this project. We have uploaded the text document and the logo we which to incorporate into this brochure.Brochure should include all our office address's (located at www.kemtrix.com.au)

Target Market(s)

Corporate, education, fitness, advertising, digital signage

Colors
0255a3
0455a3

Requirements
Must have
• Be easy to read, clean and tidy and be visually captivating.
• Promote our business as a knowlege based market leader
• Include the text we have already prepared
• Have our office addressed and contact numbers
• Include our corporate colours (www.kemtrix.com.au)
Nice to have
• Be easy to read
• Make potential customers "want to read it"
• We have the ZELK logo in AI and EPS format if needed

```html
<!DOCTYPE html>
<html lang="en">
<head>
<meta charset="utf-8">
<title>ZELK LED Wall Buyers Guide – Spread</title>
<link href="https://fonts.googleapis.com/css2?family=Montserrat:wght@400;500;600;700&display=swap" rel="stylesheet">
<style>
  :root {
    --brand-blue: #0455a3;
    --brand-blue-light: #2f7bd0;
    --navy: #0b1f5c;
    --navy-deep: #06123d;
    --ink: #2c2f36;
    --body: #5a5f69;
    --paper: #ffffff;
    --backdrop: #dcdcdc;
    --card-shadow: rgba(20, 30, 60, 0.18);
  }
  * { box-sizing: border-box; margin: 0; padding: 0; }
  html, body { width: 1200px; height: 900px; overflow: hidden; }
  body {
    background: var(--backdrop);
    font-family: "Montserrat", sans-serif;
    color: var(--body);
    position: relative;
  }
  .spread {
    position: absolute; left: 40px; top: 54px;
    width: 1120px; height: 792px;
    display: flex;
    box-shadow: 0 10px 30px rgba(0,0,0,0.15);
  }
  .page { position: relative; width: 560px; height: 792px; background: var(--paper); overflow: hidden; }

  /* Left page */
  .page--left .backdrop-art {
    position: absolute; inset: 0;
    background:
      radial-gradient(ellipse at 85% 92%, #3f7ee0 0%, rgba(63,126,224,0) 35%),
      linear-gradient(160deg, var(--navy) 0%, var(--navy-deep) 60%, #143a9a 100%);
  }
  .page--left .content-sheet {
    position: absolute; inset: 0;
    background: var(--paper);
    clip-path: polygon(14% 0, 100% 0, 100% 80%, 74% 100%, 9% 100%, 9% 14%);
  }
  .page--left .column { position: absolute; left: 96px; top: 70px; width: 420px; }

  .lead { font-size: 8.5px; line-height: 1.55; margin-bottom: 7px; }

  .topic { display: grid; grid-template-columns: 34px 1fr; column-gap: 12px; margin-top: 18px; }
  .topic__icon { width: 30px; height: 30px; background: var(--brand-blue); display: flex; align-items: center; justify-content: center; margin-top: 4px; }
  .topic__kicker { font-size: 13px; font-weight: 500; color: var(--brand-blue-light); letter-spacing: 0.5px; line-height: 1; text-transform: uppercase; }
  .topic__title { font-size: 14px; font-weight: 700; color: var(--ink); letter-spacing: 0.5px; line-height: 1.1; text-transform: uppercase; margin-bottom: 6px; }
  .topic__title--single { color: var(--brand-blue-light); font-weight: 500; margin-bottom: 6px; }

  .bullets { list-style: none; }
  .bullets li { position: relative; padding-left: 11px; font-size: 8.5px; line-height: 1.55; margin-bottom: 5px; }
  .bullets li::before { content: ""; position: absolute; left: 0; top: 4px; width: 4px; height: 4px; border-radius: 50%; background: var(--brand-blue); }

  /* Right page */
  .page--right .photo-band { position: absolute; left: 0; top: 40px; width: 220px; height: 10px; background: var(--brand-blue); }
  .page--right .hero-photo {
    position: absolute; left: 0; top: 50px; width: 210px; height: 150px;
    background: linear-gradient(180deg, #1a1f30 0%, #3b3fa8 45%, #7d63d8 70%, #4a3fb0 100%);
  }
  .install { position: absolute; left: 240px; top: 56px; width: 290px; }

  .cards { position: absolute; left: 30px; top: 290px; width: 500px; display: flex; gap: 20px; }
  .card {
    position: relative; flex: 1; background: var(--paper);
    box-shadow: 0 4px 14px var(--card-shadow);
    border-bottom: 4px solid var(--brand-blue);
    padding: 32px 14px 16px; text-align: center; min-height: 220px;
  }
  .card__icon { position: absolute; left: 50%; top: -20px; transform: translateX(-50%); width: 40px; height: 40px; background: var(--brand-blue); display: flex; align-items: center; justify-content: center; }
  .card__kicker { font-size: 11px; font-weight: 500; color: var(--brand-blue-light); text-transform: uppercase; letter-spacing: 0.5px; }
  .card__title { font-size: 12px; font-weight: 700; color: var(--ink); text-transform: uppercase; letter-spacing: 0.5px; }
  .card__rule { width: 30px; height: 2px; background: var(--brand-blue); margin: 8px auto 10px; }
  .card p { font-size: 8px; line-height: 1.55; margin-bottom: 6px; }

  .bedding { position: absolute; left: 30px; top: 580px; width: 500px; }
  .bedding__head { border-left: 4px solid var(--brand-blue); padding-left: 10px; margin-bottom: 8px; }
  .bedding p { font-size: 8.5px; line-height: 1.55; }
  .page--right .foot-band { position: absolute; right: 0; bottom: 40px; width: 300px; height: 5px; background: var(--brand-blue); }
  .gutter { position: absolute; left: 548px; top: 0; width: 24px; height: 792px; background: linear-gradient(90deg, rgba(0,0,0,0) 0%, rgba(0,0,0,0.08) 50%, rgba(0,0,0,0) 100%); pointer-events: none; }
</style>
</head>
<body>
<div class="spread">
  <section class="page page--left">
    <div class="backdrop-art" role="img" aria-label="Abstract stock image of blue light streaks across a dark navy background"></div>
    <div class="content-sheet"></div>
    <div class="column">
      <p class="lead">As LED technology naturally loses light output capability over time, configuring for circa 30-50% brightness at initial deployment allows significant headroom to combat natural decay over the lifetime of the product.</p>
      <p class="lead">When designing spaces that include LED technology, care should be taken to avoid direct light affecting the display and affecting colour and contrast.</p>

      <div class="topic">
        <div class="topic__icon"><svg width="18" height="18" viewBox="0 0 18 18" fill="none" stroke="#fff" stroke-width="1.5"><rect x="3" y="2" width="12" height="14"/><line x1="6" y1="6" x2="12" y2="6"/><line x1="6" y1="9" x2="12" y2="9"/><line x1="6" y1="12" x2="10" y2="12"/></svg></div>
        <div>
          <div class="topic__kicker">Mounting</div>
          <div class="topic__title">Requirements</div>
          <ul class="bullets">
            <li>LED display walls are built from many small tiles. They can weigh hundreds of kilograms once built, and the tolerances for uneven mounting structures are very small.</li>
            <li>It is therefore essential that the supporting structure is strong enough to support the full weight of the display and mounting hardware and constructed to tight tolerances.</li>
            <li>Should a recessed mounting solution be preferred, manufacturer's guidelines around rear clearance should be followed to allow sufficient airflow and service access.</li>
            <li>Zelk Visual Systems provide mounting solutions that are unique and reliable. Mounting options for LED displays include wall mount, ceiling mount (fly) and floor mount options.</li>
          </ul>
        </div>
      </div>

      <div class="topic">
        <div class="topic__icon"><svg width="18" height="18" viewBox="0 0 18 18" fill="none" stroke="#fff" stroke-width="1.6"><line x1="3" y1="3" x2="15" y2="15"/><line x1="15" y1="3" x2="3" y2="15"/><circle cx="9" cy="9" r="3"/></svg></div>
        <div>
          <div class="topic__kicker">Service</div>
          <div class="topic__title">Access</div>
          <ul class="bullets">
            <li>Will there be access from the front or the rear of the video wall for servicing? LED solutions are available in front, rear and dual service configurations.</li>
            <li>We will advise what the best service access solution will be depending on the physical mounting location we recommend for your LED display.</li>
          </ul>
        </div>
      </div>

      <div class="topic">
        <div class="topic__icon"><svg width="18" height="18" viewBox="0 0 18 18" fill="none" stroke="#fff" stroke-width="1.6" stroke-linecap="round"><path d="M5.5 5.5a5 5 0 1 0 7 0"/><line x1="9" y1="2.5" x2="9" y2="8.5"/></svg></div>
        <div>
          <div class="topic__title topic__title--single">Power</div>
          <ul class="bullets">
            <li>LED display technology requires special consideration for power. The exact power requirement for each LED display can vary significantly depending on the size of the display, however it is normal for an LED wall to require a number of outlets from a dedicated circuit.</li>
          </ul>
        </div>
      </div>

      <div class="topic">
        <div class="topic__icon"><svg width="18" height="18" viewBox="0 0 18 18"><path d="M9 2c1 3 5 5 5 9a5 5 0 0 1-10 0c0-2 1-3 2-4 0 2 1 3 2 3 0-3-1-5 1-8z" fill="#fff"/></svg></div>
        <div>
          <div class="topic__title topic__title--single">Heat</div>
          <ul class="bullets">
            <li>Consideration to heat management needs to be made when planning LED display technology deployments. The heat output varies significantly. It is dependent on the size of the screen and the mounting solution recommended. We will work with you to advise on the exact mechanical, electrical and environmental requirements of your LED display.</li>
          </ul>
        </div>
      </div>
    </div>
  </section>

  <section class="page page--right">
    <div class="photo-band"></div>
    <div class="hero-photo" role="img" aria-label="Stock photo of a large LED video wall showing a colourful field of flowers in a venue"></div>

    <div class="install">
      <div class="topic__kicker">Installation</div>
      <div class="topic__title">Environment</div>
      <ul class="bullets">
        <li>It is essential that the installation environment is suitable to support the successful deployment of your new LED video wall. There are many high and low voltage electrical connections to be made and rigid physical structures to be installed.</li>
        <li>Zelk Visual Systems will work with you, your project stakeholders and your programme manager to ensure that the installation environment is clean, dust free and safe prior to proceeding with the installation.</li>
      </ul>
    </div>

    <div class="cards">
      <article class="card">
        <div class="card__icon"><svg width="24" height="24" viewBox="0 0 24 24" fill="none" stroke="#fff" stroke-width="1.6"><rect x="2" y="7" width="12" height="9"/><path d="M14 10h4l3 3v3h-7z"/><circle cx="6" cy="18" r="2" fill="var(--brand-blue)"/><circle cx="17" cy="18" r="2" fill="var(--brand-blue)"/></svg></div>
        <div class="card__kicker">Delivery</div>
        <div class="card__title">Timeframes</div>
        <div class="card__rule"></div>
        <p>It is normal for delivery of LED product to be 10-12 weeks from point of order. This is due to product being manufactured on order, along with the shipping time required from our factory. The standard shipping method for LED is usually by sea. Air freight is an option to shorten lead times if product is required within a shorter lead time.</p>
      </article>
      <article class="card">
        <div class="card__icon"><svg width="24" height="24" viewBox="0 0 24 24" fill="none" stroke="#fff" stroke-width="1.6" stroke-linecap="round"><line x1="18" y1="3" x2="12" y2="11"/><path d="M10 10l4 3-3 7-5-3z" fill="#fff"/><circle cx="5" cy="6" r="1.5"/><circle cx="8" cy="3" r="1"/></svg></div>
        <div class="card__title">Cleaning</div>
        <div class="card__rule"></div>
        <p>Should the LED display require cleaning, specialist measures should be followed to carry out the required work. As seen throughout this document, LED technology is easily damaged if handled incorrectly.</p>
      </article>
      <article class="card">
        <div class="card__icon"><svg width="24" height="24" viewBox="0 0 24 24" fill="none" stroke="#fff" stroke-width="1.6" stroke-linejoin="round"><rect x="5" y="4" width="13" height="16"/><path d="M8 12l3 3 5-6"/></svg></div>
        <div class="card__kicker">Acceptance</div>
        <div class="card__title">Criteria</div>
        <div class="card__rule"></div>
        <p>LED manufacturers offer varied criteria for acceptable quantities of defective LED pixels in a display as standard.</p>
        <p>Zelk Visual Systems commits to providing you with a pixel perfect display solution at time of sign off, and at completion of the bedding in support period, ensuring you are fully satisfied.</p>
      </article>
    </div>

    <div class="bedding">
      <div class="bedding__head">
        <div class="topic__kicker">Bedding-In</div>
        <div class="topic__title" style="margin-bottom:0">Support</div>
      </div>
      <p>Even allowing for the additional offsite testing prior to installation on your site, the final shipping process, installation procedure and environmental conditions for the fully commissioned solution may carry risk of component failures. Although component issues or failures are extremely minimal, we expect any component issues to be naturally uncovered within the first 4 weeks of normal operation.</p>
    </div>
    <div class="foot-band"></div>
  </section>
  <div class="gutter"></div>
</div>
</body>
</html>
```